Squeeze page design

We need to design some squeeze pages for our list building campaigns. We use Ledgerbay as our crm. Our squeeze pages really suck. We simply need to design some pages that look better and will convert, better than what we are currently using.
The landing page that we are trying to replace can be seen at:
http://shieldworksco.example/multi-family-landing-1
The sign up page that we need to replace is:
http://shieldworksco.example/free-multi-family-offer
Our thought is that the landing page and sign up page should be combined into a single squeeze page that will improve conversions - conversions being sign ups.
Updates
Project Deadline Extended
Reason: I have had some requests to extend my deadline and I need to have some updates made to some of the submissions. Thank you.
Industry/Entity Type
Building
Look and feel
Each slider illustrates characteristics of the customer's brand and the style your logo design should communicate.

```html
<!DOCTYPE html>
<html lang="en">
<head>
<meta charset="utf-8">
<title>Shieldworks Co – Multi Family Security</title>
<link href="https://fonts.googleapis.com/css2?family=Open+Sans:wght@400;600;700&family=Noto+Serif:wght@400;700&display=swap" rel="stylesheet">
<style>
:root{
  --outer:#262626;
  --topbar:#f3f3f3;
  --header-a:#1d6a95;
  --header-b:#0e3c58;
  --nav-a:#f4f4f4;
  --nav-b:#d9d9d9;
  --ink:#222;
  --muted:#666;
  --faint:#b5b5b5;
  --link:#2a7ab5;
  --accent:#e0a100;
  --cyan:#34b4d9;
  --section:#f0f0f0;
  --navy:#0b3a5e;
  --footer-a:#1a5680;
  --footer-b:#0d3350;
  --bottom:#0a2a44;
}
*{box-sizing:border-box;margin:0;padding:0}
html,body{width:1200px;height:2375px;overflow:hidden;background:var(--outer);font-family:"Open Sans",Arial,sans-serif;color:var(--ink)}
.page{position:relative;width:1022px;height:2375px;margin-left:89px;background:#fff;overflow:hidden}
.abs{position:absolute}
.topbar{left:0;top:0;width:1022px;height:43px;background:var(--topbar)}
.toplinks{left:14px;top:12px;font-size:13px;display:flex;gap:22px}
.login{right:16px;top:0;width:106px;height:35px;background:#111;color:#fff;font-weight:700;font-size:15px;text-align:center;line-height:35px;border-radius:0 0 3px 3px}
.header{left:0;top:43px;width:1022px;height:133px;background:linear-gradient(180deg,var(--header-a),var(--header-b))}
.brand{left:22px;top:30px;display:flex;align-items:center;gap:8px}
.brand-mark{width:22px;height:22px;border-radius:50%;background:#fff}
.brand-name{color:#fff;font-weight:700;font-size:20px}
.tagline{left:150px;top:74px;color:#fff;font-weight:600;font-size:16px;letter-spacing:.5px}
.badge{right:15px;top:92px;width:212px;height:30px;background:#1e2327;border-radius:3px}
.nav{left:0;top:176px;width:1022px;height:43px;background:linear-gradient(180deg,var(--nav-a),var(--nav-b));font-size:13.5px}
.nav ul{list-style:none;display:flex;gap:36px;position:absolute;left:22px;top:12px}
.cart{right:20px;top:12px;color:var(--cyan);display:flex;gap:6px;align-items:center}
.hero{left:0;top:236px;width:1022px;height:462px;background:linear-gradient(90deg,#e6e6e6,#f5f5f5 40%,#dcdcdc)}
.hero-photo{left:488px;top:0;width:534px;height:462px;background:linear-gradient(100deg,#c98a2c,#e3a64a 50%,#b87622)}
.hero h1{left:28px;top:85px;font-family:"Noto Serif",Georgia,serif;font-weight:400;font-size:40px;line-height:46px;color:#17405e}
.hero p{left:28px;top:207px;width:380px;font-family:"Noto Serif",Georgia,serif;font-size:15px;line-height:19px;color:#333}
.guarantee{left:28px;top:329px;width:230px;height:46px;background:var(--accent);border-radius:4px;font-family:"Noto Serif",Georgia,serif;font-weight:700;font-size:18px;line-height:46px;padding-left:17px;color:#222}
.guarantee svg{position:absolute;right:18px;top:12px}
.features{left:0;top:698px;width:1022px;height:500px;background:var(--section)}
.feature h3{font-size:15px;font-weight:600;color:#111}
.thumb{position:absolute;top:76px;width:289px;height:160px;border:6px solid #fff;box-shadow:0 2px 6px rgba(0,0,0,.35)}
.thumb .play{position:absolute;left:50%;top:50%;transform:translate(-50%,-50%)}
.thumb-title{position:absolute;left:4px;top:2px;color:var(--cyan);font-weight:700;font-size:14px;line-height:17px;background:rgba(0,0,0,.45);padding:1px 3px}
.tab{position:absolute;top:264px;width:209px;height:38px;background:#dedede;font-size:14px;line-height:38px;padding-left:10px;color:#444}
.lead{position:absolute;top:330px;width:250px;font-size:12px;line-height:16px;color:#222}
.lead b{font-weight:700}
.readmore{position:absolute;top:404px;font-size:12.5px;color:var(--link);text-decoration:underline}
.offer{left:699px;top:76px;width:304px;height:356px;background:linear-gradient(180deg,#e9e9e9,#d3d3d3);border:1px solid #c7c7c7}
.offer-head{height:41px;background:linear-gradient(180deg,#1d6a95,#0e3c58);color:#fff;font-weight:600;font-size:16px;line-height:41px;padding-left:42px;position:relative}
.offer-head svg{position:absolute;left:14px;top:11px}
.offer label{display:block;position:absolute;left:12px;font-size:11px;color:#777}
.offer .field{position:absolute;left:12px;width:269px;height:27px;background:#fff;border:1px solid #ddd}
.submit{position:absolute;left:13px;top:308px;width:108px;height:38px;background:#222;color:#fff;font-weight:700;font-size:16px;text-align:center;line-height:38px;border-radius:3px}
.products h2{position:absolute;left:0;top:1262px;width:1022px;text-align:center;font-weight:400;font-size:27px;color:#333}
.products p{position:absolute;left:30px;top:1310px;width:962px;text-align:center;font-size:11px;line-height:18px;color:var(--faint)}
.card{position:absolute;top:1433px;width:307px;height:142px;border-radius:3px;overflow:hidden;color:#fff}
.card b{position:absolute;left:14px;top:66px;font-size:15px;font-weight:700;line-height:18px;text-transform:uppercase}
.card span{position:absolute;left:14px;top:108px;width:170px;font-size:8.5px;line-height:11px;text-transform:uppercase;color:#ddd}
.testimonials{left:0;top:1631px;width:1022px;height:327px;background:#f2f2f2}
.say{position:absolute;left:38px;top:58px;width:946px;text-align:center;font-size:10.5px;font-weight:700;letter-spacing:1.5px}
.say::before,.say::after{content:"";position:absolute;top:8px;width:358px;height:1px;background:#ccc}
.say::before{left:0}.say::after{right:0}
.quote{position:absolute;left:38px;top:101px;width:942px;height:149px;background:#e6e7e5;border:1px solid #d2d2d2;border-radius:3px}
.quote svg{position:absolute;left:26px;top:26px}
.quote h4{position:absolute;left:96px;top:28px;font-size:14px;font-weight:600}
.quote p{position:absolute;left:96px;top:56px;width:820px;font-size:12px;line-height:19px;color:#333}
.quote cite{position:absolute;right:28px;top:120px;font-style:normal;font-size:13px;color:#1d6a95}
.dots{position:absolute;left:476px;top:269px;display:flex;gap:10px}
.dots i{width:12px;height:12px;border-radius:50%;background:#ccc;display:block}
.dots i:last-child{background:#999}
.featured{left:0;top:1958px;width:1022px;height:128px;background:var(--navy)}
.featured h5{position:absolute;left:0;top:22px;width:1022px;text-align:center;color:#fff;font-size:15px;font-weight:600}
.press{position:absolute;top:64px;height:40px;background:#e8e8e8;border-radius:2px}
.footer{left:0;top:2086px;width:1022px;height:238px;background:linear-gradient(180deg,var(--footer-a),var(--footer-b))}
.col{position:absolute;top:50px;color:#fff}
.col h6{font-size:14.5px;font-weight:600;padding-bottom:6px;border-bottom:1px solid #3f7aa3;display:inline-block;margin-bottom:12px}
.col li{list-style:none;font-size:12.5px;line-height:20px;color:#e4eef5}
.col p{font-size:12.5px;line-height:20px;color:#e4eef5}
.social{display:grid;grid-template-columns:repeat(4,18px);gap:14px 14px;margin-top:4px}
.social i{width:16px;height:16px;background:#3f6f92;border-radius:2px;display:block}
.bottom{left:0;top:2324px;width:1022px;height:51px;background:var(--bottom);color:#fff;font-size:12.5px}
.bottom span{position:absolute;left:30px;top:17px}
.pay{position:absolute;top:15px;width:40px;height:24px;background:#f2f2f2;border-radius:2px}
</style>
</head>
<body>
<div class="page">
  <div class="abs topbar">
    <div class="abs toplinks"><span>FAQ</span><span>Store / Installer Locator</span><span>Affiliates</span><span>Register</span></div>
    <div class="abs login">LOGIN</div>
  </div>

  <header class="abs header">
    <div class="abs brand"><span class="brand-mark"></span><span class="brand-name">Shieldworks Co</span></div>
    <div class="abs tagline">Protection You Can Trust</div>
    <div class="abs badge"></div>
  </header>

  <nav class="abs nav">
    <ul><li>Home</li><li>Buy Online</li><li>Preventing Break-Ins</li><li>Testimonials</li><li>About us</li><li>Our Blog</li></ul>
    <div class="abs cart">VIEW CART
      <svg width="18" height="16" viewBox="0 0 18 16"><path d="M1 2h3l2 8h9l2-6H5" fill="none" stroke="#34b4d9" stroke-width="2"/><circle cx="7" cy="13.5" r="1.6" fill="#34b4d9"/><circle cx="14" cy="13.5" r="1.6" fill="#34b4d9"/></svg>
    </div>
  </nav>

  <section class="abs hero">
    <div class="abs hero-photo" role="img" aria-label="Wooden door standing open, showing a chrome lever handle and deadbolt lock"></div>
    <h1 class="abs">Guaranteed to<br>Save you money</h1>
    <p class="abs">EZ Shield Protects your Residents with one easy-to-Install Kit<br>Available in colors to match your locks.An attractive and affordable resident retention tool.</p>
    <div class="abs guarantee">OUR GURANTEE
      <svg width="18" height="22" viewBox="0 0 18 22"><path d="M4 10V6a5 5 0 0 1 10 0" fill="none" stroke="#fff" stroke-width="2.4"/><rect x="1" y="10" width="16" height="12" rx="2" fill="#fff"/></svg>
    </div>
  </section>

  <section class="abs features">
    <div class="abs feature" style="left:22px;top:48px"><h3>Apartment Security Starts Here</h3></div>
    <div class="thumb" style="left:22px;background:linear-gradient(90deg,#2b2b2b,#4a4a4a 50%,#1a1a1a)" role="img" aria-label="Video still of a dark apartment door at night">
      <svg class="play" width="56" height="56" viewBox="0 0 56 56"><circle cx="28" cy="28" r="28" fill="#fff"/><path d="M22 17l17 11-17 11z" fill="#111"/></svg>
    </div>
    <div class="tab" style="left:19px">Why Secure Your Doors?</div>
    <p class="lead" style="left:22px"><b>Safety is the #1</b><br>reason residents site for moving More than 85% of all break-ins are through a door.</p>
    <span class="readmore" style="left:22px">Read More</span>

    <div class="abs feature" style="left:359px;top:48px"><h3>Why Police Trust Us</h3></div>
    <div class="thumb" style="left:359px;background:linear-gradient(90deg,#8c8a84,#b3aea4 50%,#7c7b76)" role="img" aria-label="Video still of a police officer speaking outdoors">
      <div class="thumb-title">EZ Shield Police Test and<br>Recommendation</div>
      <svg class="play" width="56" height="56" viewBox="0 0 56 56"><circle cx="28" cy="28" r="28" fill="#fff"/><path d="M22 17l17 11-17 11z" fill="#111"/></svg>
    </div>
    <div class="tab" style="left:356px">Why Secure Your Doors?</div>
    <p class="lead" style="left:359px"><b>Police Tested and Recommended</b><br>Police and other independent sources have thoroughly tested and recommend our products because they work.</p>
    <span class="readmore" style="left:359px">Read More</span>

    <form class="abs offer">
      <div class="offer-head">
        <svg width="20" height="20" viewBox="0 0 20 20"><rect x="1" y="3" width="14" height="16" fill="none" stroke="#fff" stroke-width="1.8"/><path d="M7 13l2-4 8-8 2 2-8 8z" fill="#fff"/></svg>
        Multi Family Free offer
      </div>
      <label style="top:60px">Property Name:</label><div class="field" style="top:81px"></div>
      <label style="top:120px">First Name:</label><div class="field" style="top:141px"></div>
      <label style="top:183px">Last Name:</label><div class="field" style="top:204px"></div>
      <label style="top:246px">Email:</label><div class="field" style="top:265px"></div>
      <div class="submit">SUBMIT</div>
    </form>
  </section>

  <section class="products">
    <h2>Available For <b style="font-weight:600">All Doors</b> and <b style="font-weight:600">Budgets</b></h2>
    <p>It is a long established fact that a reader will be distracted by the readable content of a page when looking at its layout. The point of using Lorem Ipsum is that it has a more-or-less normal distribution of letters, as opposed to using 'Content here, content here', making it look like readable English. Many desktop publishing packages and web page editors now use Lorem Ipsum as their default model text, and a search for 'lorem ipsum' will uncover many web sites still in their infancy. Various versions have evolved over the years.</p>
    <div class="card" style="left:20px;background:linear-gradient(90deg,#0f3550,#2a5d7e 55%,#b9bcbf)" role="img" aria-label="EZ Shield combo set with steel door reinforcement plates">
      <b>EZ Shield<br>Combo Set</b><span>Total door security that guards every weak point of your door.</span>
    </div>
    <div class="card" style="left:357px;background:linear-gradient(90deg,#050505,#1c1c1c 60%,#0a0a0a)" role="img" aria-label="Frame-Fix door jamb repair strip">
      <b>Frame-Fix</b><span>The next generation frame repair, quick and inexpensive to install.</span>
    </div>
    <div class="card" style="left:693px;background:linear-gradient(90deg,#2c3540,#4d4037 55%,#d7d7d7)" role="img" aria-label="Shield Latch installed on a door edge">
      <b>Shield Latch</b><span>Barely visible once installed, effective and economical security.</span>
    </div>
  </section>

  <section class="abs testimonials">
    <div class="say">OUR CUSTOMERS SAY IT BEST:</div>
    <blockquote class="quote">
      <svg width="48" height="36" viewBox="0 0 48 36"><path d="M0 36V20C0 8 6 2 18 0v7c-6 2-9 6-9 12h9v17zM26 36V20C26 8 32 2 44 0v7c-6 2-9 6-9 12h9v17z" fill="#fff"/></svg>
      <h4>Police Recommended</h4>
      <p>The Ventura Police gave us the information on your door shield, of course this was after our front door was kicked in and a 350lb. safe was carried out. We are now in Escrow and looking forward to moving north. When we get settled and find a new home we will be contacting you to learn more about your new products and keeping us safe. Thanks Again.</p>
      <cite>Mark and Dana R – Ventura, CA</cite>
    </blockquote>
    <div class="dots"><i></i><i></i><i></i></div>
  </section>

  <section class="abs featured">
    <h5>AS FEATURED ON</h5>
    <div class="press" style="left:73px;width:41px"></div>
    <div class="press" style="left:148px;width:108px"></div>
    <div class="press" style="left:288px;width:108px"></div>
    <div class="press" style="left:431px;width:231px"></div>
    <div class="press" style="left:700px;width:82px"></div>
    <div class="press" style="left:810px;width:106px;background:#2a2a2a"></div>
  </section>

  <footer class="abs footer">
    <div class="col" style="left:38px"><h6>RESOURCES</h6><ul><li>Resources</li><li>Testimonials</li><li>Competition</li><li>Media Coverage</li><li>Crime Prevention</li></ul></div>
    <div class="col" style="left:199px"><h6>ABOUT US</h6><ul><li>Affiliate Program</li><li>FAQ</li><li>About Us</li><li>Contact Us</li></ul></div>
    <div class="col" style="left:361px"><h6>COMMUNITY</h6><ul><li>Returns/Exchanges</li><li>Privacy</li><li>Warranty Information</li><li>Become A Distributor</li></ul></div>
    <div class="col" style="left:551px"><h6>SUPPORT US</h6><div class="social"><i></i><i></i><i></i><i></i><i></i><i></i><i></i><i></i></div></div>
    <div class="col" style="left:733px;width:260px"><h6>CONTACT US</h6><p>US Patent Numbers 7,412,903 / 7,958,271</p><p style="margin-top:18px">Information Sources: FBI Uniform Crime Report, Bureau of Justice Statistics and U.S. Department of Justice.</p></div>
  </footer>

  <div class="abs bottom">
    <span>© 2005-2014 Shieldworks Co LLC. All rights reserved.</span>
    <div class="pay" style="left:811px"></div>
    <div class="pay" style="left:857px"></div>
    <div class="pay" style="left:903px"></div>
    <div class="pay" style="left:949px"></div>
  </div>
</div>
</body>
</html>
```